Postcard Design

The name of my company (independently owned) is Harbor Stride Wellness. My company is located in Flagler Beach, Florida less than two short blocks to the beach. We offer massage therapy, personal training and JOYfully Strong Drills near the beach. My specialty is kettlebell training, working with athletic types, and sports massage. My class won 2nd place in the 2010 Townlooker "Top Routine of 2010, NYC." I am a Federal Vigor and Endurance Guild Vigor and Endurance Expert, considered the certification of distinction within the fitness community. I want to have a postcard that is placed in goody bags at local sporting events advertising my product and offering a $20.00 discount if they bring the post card with them to my business.

Services offered: Swedish Massage, Deep Tissue Massage, Aromatherapy, Sports Massage, Kinesiotaping, Personal Training, and JOYfully Strong Drills.

Target Market(s)

Clients who enjoy massage and fitness. While not necessarily athletes, there needs to be a hint of athleticism in post card.

Industry/Entity Type

Training

Requirements
Must have
• Business address, phone number and webpage:
418 West 7th Avenue Suite #3, Flagler Beach, FL (386) 555-0172 www.harborstridewellness.example

A catch phrase stating that if you bring the card to establishment you will receive $20.00 off your massage that cannot be combined with any other offer.

Fun and beachy feel.

Information on two sides of card.

A header stating that we offer Massage Therapy and JOYful Movement

Photo/s that illustrate both massage AND fitness

Should not have
• Color front and black-and-white, but catchy back side.

```html
<!DOCTYPE html>
<html lang="en">
<head>
<meta charset="utf-8">
<title>Harbor Stride Wellness Postcard</title>
<link rel="stylesheet" href="https://fonts.googleapis.com/css2?family=Arimo:wght@400;700&family=Oswald:wght@500&display=swap">
<style>
  :root {
    --stage: #8a8a8a;
    --brand-blue: #2b6fd6;
    --band-blue: #4f8fe3;
    --panel-blue: #4d96ef;
    --leaf-green: #3f9a1e;
    --lime: #9be03c;
    --white: #ffffff;
    --sand: #cdb79c;
    --sea: #9fd7d5;
  }
  * { box-sizing: border-box; margin: 0; padding: 0; }
  html, body { width: 1200px; height: 600px; overflow: hidden; }
  body { background: var(--stage); font-family: "Arimo", Arial, sans-serif; position: relative; }

  .postcard-front, .postcard-back { position: absolute; top: 105px; height: 388px; overflow: hidden; }
  .postcard-front { left: 95px; width: 505px; background: var(--white); }
  .postcard-back { left: 600px; width: 505px; }

  .runners-photo {
    position: absolute; left: 0; top: 0; width: 290px; height: 388px;
    background: linear-gradient(90deg, #c9e6ea 0%, #bfe3e4 55%, rgba(255,255,255,0) 100%),
                linear-gradient(180deg, #eef7fa 0%, var(--sea) 45%, #e3d6c4 100%);
  }

  .offer-column {
    position: absolute; left: 262px; width: 212px; top: 0; text-align: center;
    display: flex; flex-direction: column; align-items: center;
  }
  .brand-lockup { margin-top: 38px; display: flex; flex-direction: column; align-items: center; }
  .brand-mark { width: 26px; height: 26px; border-radius: 50%; background: #f4e24a; margin-bottom: 6px; }
  .brand-name { color: var(--brand-blue); font-weight: 700; font-size: 20px; line-height: 1.05; width: 170px; }
  .brand-tagline {
    color: var(--leaf-green); font-weight: 700; font-size: 10px; margin-top: 8px; white-space: nowrap;
    border-top: 2px solid var(--leaf-green); padding: 2px 2px 0;
  }
  .brand-phone { color: var(--brand-blue); font-weight: 700; font-size: 15px; letter-spacing: .5px; }

  .offer-intro, .offer-terms, .offer-landmark { color: var(--leaf-green); font-weight: 700; font-size: 10.5px; line-height: 1.25; }
  .offer-intro { margin-top: 5px; }
  .offer-amount { font-family: "Oswald", "Arial Narrow", sans-serif; color: var(--brand-blue); font-size: 36px; line-height: 1.05; letter-spacing: .5px; }
  .offer-amount sup { font-size: 18px; vertical-align: 14px; }
  .offer-url {
    display: inline-block; margin-top: 8px; background: var(--band-blue); color: var(--white);
    font-weight: 700; font-size: 10px; padding: 4px 7px; white-space: nowrap;
  }
  .address { color: var(--brand-blue); font-weight: 700; font-size: 13px; line-height: 1.2; margin-top: 6px; white-space: nowrap; }
  .offer-landmark { color: var(--brand-blue); margin-top: 3px; }

  .services-band {
    position: absolute; left: 0; bottom: 0; width: 505px; height: 40px;
    background: rgba(79,143,227,.92); color: var(--white);
    font-size: 9.5px; line-height: 14px; text-align: center; padding-top: 6px;
  }
  .services-band .sep { display: inline-block; width: 2px; height: 10px; background: var(--lime); margin: 0 2px; vertical-align: -1px; }

  .beach-photo {
    position: absolute; inset: 0;
    background: linear-gradient(180deg, var(--panel-blue) 0%, var(--panel-blue) 52%, #a8c9e6 62%, #7fb3c7 68%, #d9c7b0 74%, var(--sand) 100%);
  }
  .massage-photo { position: absolute; left: 25px; top: 0; width: 182px; height: 120px; background: linear-gradient(160deg, #d8e6f2, #e9c9ad 60%, #f2f2f2); }
  .fitness-photo { position: absolute; left: 25px; top: 120px; width: 182px; height: 172px; background: linear-gradient(180deg, #3d8fe6 0%, #7ab9f0 55%, #c9a27f 80%, #dcd3c4 100%); }
  .brand-tile {
    position: absolute; left: 25px; top: 292px; width: 182px; height: 96px; background: var(--white);
    display: flex; flex-direction: column; align-items: center; justify-content: center; text-align: center;
  }
  .brand-tile .brand-mark { width: 18px; height: 18px; margin-bottom: 3px; }
  .brand-tile .brand-name { font-size: 13px; width: 170px; }
  .brand-tile .brand-tagline { font-size: 7px; margin-top: 3px; padding-top: 1px; border-top-width: 1px; }
  .brand-tile .brand-phone { font-size: 10px; }

  .location-copy {
    position: absolute; left: 218px; top: 23px; width: 278px;
    color: var(--white); font-weight: 700; font-size: 9.4px; line-height: 11.5px;
  }
</style>
</head>
<body>
  <section class="postcard-front">
    <div class="runners-photo" role="img" aria-label="Photo of two runners jogging along the beach"></div>
    <div class="offer-column">
      <div class="brand-lockup">
        <span class="brand-mark"></span>
        <div class="brand-name">Harbor Stride Wellness</div>
        <div class="brand-tagline">Massage Therapy &amp; JOYful Movement</div>
        <div class="brand-phone">(386) 555-0172</div>
      </div>
      <p class="offer-intro">Bring this card to us and receive</p>
      <p class="offer-amount"><sup>$</sup>20.00 off</p>
      <p class="offer-terms">your massage - cannot be combined<br>with any other offer.</p>
      <span class="offer-url">www.harborstridewellness.example</span>
      <p class="address">418 WEST 7TH AVENUE<br>SUITE #3, FLAGLER BEACH,FL</p>
      <p class="offer-landmark">Located directly across from the<br>Farmer's Market</p>
    </div>
    <div class="services-band">
      Swedish Massage<span class="sep"></span>Deep Tissue Massage<span class="sep"></span>Sports Massage<span class="sep"></span>Lymphatic Massage<span class="sep"></span>Aromatherapy<br>
      Kinesio Taping<span class="sep"></span>Personal Training<span class="sep"></span>JOYfully Strong Drills
    </div>
  </section>

  <section class="postcard-back">
    <div class="beach-photo" role="img" aria-label="Photo of Flagler Beach with pier and sandy shore"></div>
    <div class="massage-photo" role="img" aria-label="Photo of a therapist massaging a knee"></div>
    <div class="fitness-photo" role="img" aria-label="Photo of a woman holding a kettlebell on the beach"></div>
    <div class="brand-tile">
      <span class="brand-mark"></span>
      <div class="brand-name">Harbor Stride Wellness</div>
      <div class="brand-tagline">Massage Therapy &amp; JOYful Movement</div>
      <div class="brand-phone">(386) 555-0172</div>
    </div>
    <p class="location-copy">We are located two blocks away from historic Flagler Beach, nestled between St. Augustine and Daytona. Our pristine beaches, natural parks, open-air restaurants, and shopping make Flagler Beach the perfect destination for any visitor.&nbsp; Stop by for a massage or a bootcamp and make sure to stay a while to see why SUNCOASTTRIPS.example describes Flagler Beach as the "retro town with salty style.</p>
  </section>
</body>
</html>
```